依頼詳細
「第33回紫雲まつり」のポスター制作をお願いいたします。B2、A4、A5サイズで、デザインは同じで構いません。
昨年のデザインにとらわれず、インパクト重視の華やかなチラシにしていただけたらと思います。
記載項目
ご参考までに「昨年のポスター」をご確認下さい

昨年との変更点は、下記のとおりで、それ以外の文字も全て記載してください
・令和元年10月4日(金)5日(土)雨天の場合、順延6日(日)
・第33回紫雲まつり
・第51回瑞穂花火大会 10月5日(土)
・「県内唯一!二尺玉大花火5発」を削除
サイズ
B2
ページ数
片面
希望イメージ
• +5 0 +5
• シンプル
複雑
• 単色
カラフル
• 暗い
明るい
• 日常
高級
• 遊び心
厳粛
• 未来的
伝統的
• 女性的
男性的
希望する色
納品ファイル
• 高解像度JPG (.jpg)
• イラストレーター形式 (.ai)
補足説明
作成頂いたデザインは、チラシ、ポスターの印刷に使用するほか、当方にて一部修正して、ホームページやパンフレットの表紙などに流用いたします。
キャラクター「ころりん」を使用する場合は「(C)K.S.」を必ず付けてください
QRコードはダミーで作成してください(当選後差し替え)
依頼公開後の追記内容
■ 選んだ理由

まつり実行委員会広報委員による審議・投票により、当選を決定させていただきました。

■ 提案者全員のお礼・コメント

ご提案を頂き誠にありがとうございました。前回より作品数も多く、またレベルの高い力作ぞろいでした。ご提案くださった皆様に心より感謝申しあげます。

```html
<!DOCTYPE html>
<html lang="ja">
<head>
<meta charset="utf-8">
<title>第33回 紫雲まつり</title>
<link rel="stylesheet" href="https://fonts.googleapis.com/css2?family=Yuji+Boku&family=Noto+Sans+JP:wght@500;700;900&family=Zen+Maru+Gothic:wght@700;900&display=swap">
<style>
:root{
  --night:#0b1640;
  --night-deep:#050a24;
  --gold:#ffd21a;
  --red:#d6141e;
  --white:#ffffff;
  --purple:#4a2a86;
  --green:#2ea83a;
  --navy-text:#1a2350;
  --box-blue:#1f6fd1;
}
*{margin:0;padding:0;box-sizing:border-box}
html,body{width:849px;height:1200px;overflow:hidden;background:var(--night-deep)}
.poster{position:relative;width:849px;height:1200px;overflow:hidden;font-family:"Noto Sans JP",sans-serif;color:var(--white);
  background:radial-gradient(ellipse at 60% 40%,#1d2f78 0%,var(--night) 45%,var(--night-deep) 100%)}
.fireworks{position:absolute;inset:0 0 95px 0;
  background:radial-gradient(circle at 25% 30%,rgba(255,120,60,.35),transparent 30%),
  radial-gradient(circle at 75% 55%,rgba(255,200,80,.3),transparent 28%),
  radial-gradient(circle at 50% 85%,rgba(255,90,40,.4),transparent 35%),
  radial-gradient(circle at 85% 20%,rgba(120,200,255,.25),transparent 25%)}
.edition-badge{position:absolute;left:18px;top:14px;background:var(--red);padding:6px 14px;font-family:"Zen Maru Gothic",sans-serif;font-weight:900;font-size:30px;border-radius:4px;border:3px solid var(--gold);color:var(--gold)}
.edition-badge b{font-size:44px}
.title{position:absolute;left:130px;top:60px;writing-mode:vertical-rl;font-family:"Yuji Boku",serif;font-size:160px;line-height:1;color:var(--gold);
  -webkit-text-stroke:4px var(--red);paint-order:stroke fill;letter-spacing:-6px}
.mascot{position:absolute;left:450px;top:0;width:399px;height:500px;border-radius:0 0 40% 40%;
  background:radial-gradient(ellipse at 50% 45%,#f2e6d0 0%,#d8c7a8 55%,rgba(216,199,168,0) 75%)}
.era{position:absolute;left:560px;top:505px;font-family:"Zen Maru Gothic",sans-serif;font-weight:900;font-size:28px}
.dates{position:absolute;left:440px;top:545px;display:flex;align-items:flex-end;font-family:"Zen Maru Gothic",sans-serif;font-weight:900;color:var(--gold);line-height:1}
.dates .num{font-size:100px;-webkit-text-stroke:3px var(--red);paint-order:stroke fill}
.dates .slash{font-size:72px}
.dow{display:inline-flex;width:44px;height:44px;border-radius:50%;align-items:center;justify-content:center;font-size:26px;margin:0 10px 10px 4px;color:var(--white)}
.dow.fri{background:var(--red)}
.dow.sat{background:var(--box-blue)}
.rain-note{position:absolute;left:600px;top:662px;font-size:14px;font-weight:700}
.fireworks-strip{position:absolute;left:16px;top:485px;width:96px;height:530px;display:flex;flex-direction:column;align-items:center}
.strip-date{background:var(--white);color:var(--purple);font-weight:900;font-size:20px;width:100%;text-align:center;padding:4px 0;border-radius:4px 4px 0 0}
.strip-body{flex:1;width:100%;background:var(--purple);display:flex;flex-direction:column;align-items:center;padding:10px 0;border:3px solid var(--white);border-top:none}
.strip-edition{writing-mode:vertical-rl;color:var(--gold);font-weight:900;font-size:22px;background:var(--green);padding:6px 4px;margin-bottom:10px}
.strip-name{writing-mode:vertical-rl;font-family:"Zen Maru Gothic",sans-serif;font-weight:900;font-size:50px;line-height:1}
.strip-time{writing-mode:vertical-rl;font-size:15px;font-weight:700;margin-top:auto}
.schedule{position:absolute;left:330px;top:720px;display:flex;gap:10px}
.event{width:118px;height:260px;display:flex;flex-direction:column}
.event-tag{font-weight:900;font-size:17px;text-align:center;padding:3px 0;color:var(--white)}
.event.sat .event-tag{background:var(--box-blue)}
.event.fri .event-tag{background:var(--red)}
.event-body{flex:1;background:rgba(255,255,255,.92);color:var(--navy-text);writing-mode:vertical-rl;font-size:16px;font-weight:700;padding:10px 8px;line-height:1.5}
.event-body .hl{color:var(--red)}
.footer{position:absolute;left:0;bottom:0;width:100%;height:95px;background:var(--white);color:var(--navy-text);padding:12px 20px;display:flex;justify-content:space-between;align-items:center}
.organizer{font-size:15px;font-weight:700;line-height:1.55}
.web{display:flex;flex-direction:column;align-items:flex-end;gap:6px}
.search{display:flex;align-items:center;border:2px solid var(--navy-text);border-radius:4px;font-size:14px;font-weight:700}
.search span{padding:2px 10px}
.search i{display:block;width:30px;height:24px;background:var(--navy-text)}
.url{font-size:13px;font-weight:700}
</style>
</head>
<body>
<div class="poster">
  <div class="fireworks" role="img" aria-label="夜空に広がる花火と川辺の祭り風景の写真"></div>

  <div class="edition-badge">第<b>33</b>回</div>
  <h1 class="title">紫雲まつり</h1>

  <div class="mascot" role="img" aria-label="まつりのマスコットキャラクターのイラスト"></div>

  <div class="era">令和元年</div>
  <div class="dates">
    <span class="num">10</span><span class="slash">/</span><span class="num">4</span><span class="dow fri">金</span>
    <span class="num">5</span><span class="dow sat">土</span>
  </div>
  <div class="rain-note">※雨天の場合 順延 6日(日)</div>

  <div class="fireworks-strip">
    <div class="strip-date">10/5土</div>
    <div class="strip-body">
      <div class="strip-edition">第51回</div>
      <div class="strip-name">瑞穂花火大会</div>
      <div class="strip-time">午後8時～</div>
    </div>
  </div>

  <div class="schedule">
    <div class="event sat"><div class="event-tag">10/5土</div><div class="event-body"><span class="hl">市民総踊り</span><br>午後六時より<br>駅前大通り</div></div>
    <div class="event sat"><div class="event-tag">10/5土</div><div class="event-body"><span class="hl">よさこい踊り</span><br>瑞穂よさこい大会<br>もちまき</div></div>
    <div class="event fri"><div class="event-tag">10/4金</div><div class="event-body"><span class="hl">宵宮行列</span><br>子ども神輿<br>提灯行列</div></div>
    <div class="event fri"><div class="event-tag">10/4金</div><div class="event-body"><span class="hl">時代行列</span><br>元祖「紫雲伝説」<br>ステージ</div></div>
  </div>

  <footer class="footer">
    <div class="organizer">
      主催／紫雲まつり推進団体協議会、第33回紫雲まつり実行委員会<br>
      〒600-0000 架空県瑞穂市新屋敷1番地　TEL.0000-00-0000
    </div>
    <div class="web">
      <div class="search"><span>紫雲まつり</span><i></i></div>
      <div class="url">http://shiun-matsuri.example</div>
    </div>
  </footer>
</div>
</body>
</html>
```